GlowMoths Windows App design

We will need a designer to redesign our entire app for Windows Phone use.

Currently, we have apps available for Android and iOS, they can be downloaded here: http://www.talvorin.net/downloads/

Other than just following the same concept, we want this app to be based on the Metro design, with an about page to tell user more about this app and our services, also to design the live tile.

Included are some designs done previously by other designers.
Updates

Dear Designers,

We would be making our decision based on the main screen, where device list is loaded. 

The main direction would be the metro style design.

Best Regards,
Merrow

Reason: We have pretty good designs in, just a few more days to see if there are any new entrants.

Industry/Entity Type

Android

```html
<!DOCTYPE html>
<html lang="en">
<head>
<meta charset="utf-8">
<title>GlowMoths – Device List</title>
<link rel="stylesheet" href="https://fonts.googleapis.com/css2?family=Lato:wght@300;700&display=swap">
<style>
  :root {
    --bg: #0f4a5a;
    --tile: #00b5dd;
    --tile-edge: #38cbe9;
    --tile-strip: #33c6e6;
    --tile-active: #38dcfe;
    --tile-active-strip: #66e5ff;
    --white: #ffffff;
    --muted: #9fb0b6;
    --footer: #3d6e7a;
  }
  * { margin: 0; padding: 0; box-sizing: border-box; }
  html, body { width: 675px; height: 1200px; overflow: hidden; background: var(--bg); }
  .screen {
    position: relative; width: 675px; height: 1200px; overflow: hidden;
    background: var(--bg); font-family: "Lato", sans-serif; color: var(--white);
  }
  .header {
    position: absolute; left: 37px; right: 25px; top: 128px;
    display: flex; justify-content: space-between; align-items: center;
  }
  .welcome { font-weight: 700; font-size: 35px; letter-spacing: 0.5px; }
  .logout { font-weight: 700; font-size: 35px; color: var(--muted); }
  .device-list { position: absolute; left: 35px; top: 198px; width: 615px; list-style: none; }
  .device {
    position: relative; height: 106px; margin-bottom: 20.2px;
    background: var(--tile); border: 1px solid var(--tile-edge);
  }
  .device.is-active { background: var(--tile-active); border-color: var(--tile-active-strip); }
  .device-icon { position: absolute; left: 29px; top: 20px; width: 66px; height: 66px; }
  .device-code {
    position: absolute; left: 119px; top: 8px; font-weight: 700; font-size: 43px;
    text-shadow: 0 1px 2px rgba(0,0,0,0.15);
  }
  .device-address {
    position: absolute; left: 119px; top: 60px; width: 455px;
    font-weight: 300; font-size: 25.5px; white-space: nowrap; overflow: hidden;
  }
  .device-open {
    position: absolute; right: 0; top: 0; width: 35px; height: 100%;
    background: var(--tile-strip); display: flex; align-items: center; justify-content: center;
  }
  .device.is-active .device-open { background: var(--tile-active-strip); }
  .footer {
    position: absolute; left: 0; bottom: 0; width: 675px; height: 98px;
    background: var(--footer); display: flex; align-items: center; padding-left: 33px;
    font-weight: 700; font-size: 33px;
  }
</style>
</head>
<body>
<main class="screen">
  <header class="header">
    <span class="welcome">WELCOME</span>
    <span class="logout">[LOGOUT]</span>
  </header>

  <ul class="device-list">
    <li class="device is-active">
      <svg class="device-icon" viewBox="0 0 66 66"><circle cx="33" cy="33" r="31.5" fill="none" stroke="#fff" stroke-width="2"/><circle cx="33" cy="33" r="15" fill="none" stroke="#fff" stroke-width="7"/></svg>
      <span class="device-code">PTD</span>
      <span class="device-address">T1 Skyward Cresent,Singapore</span>
      <span class="device-open"><svg width="8" height="8" viewBox="0 0 8 8"><path d="M1 1 L7 4 L1 7 Z" fill="#fff"/></svg></span>
    </li>
    <li class="device">
      <svg class="device-icon" viewBox="0 0 66 66"><circle cx="33" cy="33" r="31.5" fill="none" stroke="#fff" stroke-width="2"/><circle cx="33" cy="33" r="15" fill="none" stroke="#fff" stroke-width="7"/></svg>
      <span class="device-code">GUZ</span>
      <span class="device-address">20 Palmvale Crescent, Singapore</span>
      <span class="device-open"><svg width="8" height="8" viewBox="0 0 8 8"><path d="M1 1 L7 4 L1 7 Z" fill="#fff"/></svg></span>
    </li>
    <li class="device">
      <svg class="device-icon" viewBox="0 0 66 66"><circle cx="33" cy="33" r="31.5" fill="none" stroke="#fff" stroke-width="2"/><circle cx="33" cy="33" r="15" fill="none" stroke="#fff" stroke-width="7"/></svg>
      <span class="device-code">GBB</span>
      <span class="device-address">113 Linden Quay St, Singapore</span>
      <span class="device-open"><svg width="8" height="8" viewBox="0 0 8 8"><path d="M1 1 L7 4 L1 7 Z" fill="#fff"/></svg></span>
    </li>
    <li class="device">
      <svg class="device-icon" viewBox="0 0 66 66"><circle cx="33" cy="33" r="31.5" fill="none" stroke="#fff" stroke-width="2"/><circle cx="33" cy="33" r="15" fill="none" stroke="#fff" stroke-width="7"/></svg>
      <span class="device-code">PA</span>
      <span class="device-address">333, Marwood Hill Avenue 1, Singapore</span>
      <span class="device-open"><svg width="8" height="8" viewBox="0 0 8 8"><path d="M1 1 L7 4 L1 7 Z" fill="#fff"/></svg></span>
    </li>
    <li class="device">
      <svg class="device-icon" viewBox="0 0 66 66"><circle cx="33" cy="33" r="31.5" fill="none" stroke="#fff" stroke-width="2"/><circle cx="33" cy="33" r="15" fill="none" stroke="#fff" stroke-width="7"/></svg>
      <span class="device-code">PTD</span>
      <span class="device-address">31 Fernbrook, Cresent, Singapore</span>
      <span class="device-open"><svg width="8" height="8" viewBox="0 0 8 8"><path d="M1 1 L7 4 L1 7 Z" fill="#fff"/></svg></span>
    </li>
    <li class="device">
      <svg class="device-icon" viewBox="0 0 66 66"><circle cx="33" cy="33" r="31.5" fill="none" stroke="#fff" stroke-width="2"/><circle cx="33" cy="33" r="15" fill="none" stroke="#fff" stroke-width="7"/></svg>
      <span class="device-code">PA</span>
      <span class="device-address">21 Harlow Town Hall Rd, Singapore</span>
      <span class="device-open"><svg width="8" height="8" viewBox="0 0 8 8"><path d="M1 1 L7 4 L1 7 Z" fill="#fff"/></svg></span>
    </li>
    <li class="device">
      <svg class="device-icon" viewBox="0 0 66 66"><circle cx="33" cy="33" r="31.5" fill="none" stroke="#fff" stroke-width="2"/><circle cx="33" cy="33" r="15" fill="none" stroke="#fff" stroke-width="7"/></svg>
      <span class="device-code">PC</span>
      <span class="device-address">10 Kestrel Business Park Central 2,</span>
      <span class="device-open"><svg width="8" height="8" viewBox="0 0 8 8"><path d="M1 1 L7 4 L1 7 Z" fill="#fff"/></svg></span>
    </li>
  </ul>

  <footer class="footer">TOTAL ASSETS : 225</footer>
</main>
</body>
</html>
```